Brambel Logging Business Card Design Project

We need a new company business card. We provide professional timber harvesting (logging) and forest management services. I'm open to any creative design. Most company caps and shirts are navy blue and Light grey. Logo does not necessarily have to contain those colors. Logo containing picture of logging equipment, log truck, trees, or logs are acceptable. Be creative. Final logo should communicate our company's pride and professionalism in the East Texas Timber Industry.
Updates

Target Market(s)

Timber owners, sawmills, and forestry professionals

Industry/Entity Type

Business

Requirements
Must have
• Must have Contact Info.
Phone: 936-402-5817
address: PO Box 8462
Cedar Hollow, Tx 75912
www.mbrambellogging.example
mbrambellogging@mailbox.example
Owner: Marv Brambel

Or design must leave room for this info.

```html
<!DOCTYPE html>
<html lang="en">
<head>
<meta charset="utf-8">
<title>Brambel Logging Business Card</title>
<link rel="stylesheet" href="https://fonts.googleapis.com/css2?family=Arimo:wght@400;700&display=swap">
<style>
  :root {
    --bg: #5b5b5b;
    --frame-dark: #2a0c07;
    --frame-mid: #4a1a0f;
    --frame-light: #5e2414;
    --panel: #86c02a;
    --ink: #1a1a12;
    --ink-light: #ffffff;
  }
  * { box-sizing: border-box; margin: 0; padding: 0; }
  html, body { width: 1200px; height: 960px; overflow: hidden; }
  body {
    background: var(--bg);
    font-family: "Arimo", Arial, sans-serif;
    position: relative;
  }
  .card {
    position: absolute;
    width: 540px;
    height: 320px;
    border-radius: 20px;
    padding: 30px 34px;
    background: linear-gradient(120deg, var(--frame-dark) 0%, var(--frame-light) 35%, var(--frame-mid) 60%, var(--frame-dark) 100%);
    box-shadow: 0 14px 28px rgba(0,0,0,0.45);
  }
  .card-front { left: 60px; top: 130px; }
  .card-back { left: 600px; top: 510px; }
  .panel {
    width: 100%;
    height: 100%;
    background: var(--panel);
    display: flex;
    flex-direction: column;
    align-items: center;
    justify-content: center;
    text-align: center;
    color: var(--ink);
  }
  .company-name {
    font-weight: 400;
    font-size: 30px;
    line-height: 1.2;
    letter-spacing: 0.2px;
  }
  .owner-name {
    font-weight: 700;
    font-size: 19px;
    letter-spacing: 0.3px;
  }
  .owner-title {
    font-size: 11px;
    color: var(--ink-light);
    margin-top: 2px;
    margin-bottom: 18px;
  }
  .contact-line {
    font-size: 14px;
    line-height: 1.5;
  }
</style>
</head>
<body>
  <section class="card card-front" aria-label="Business card front">
    <div class="panel">
      <h1 class="company-name">M.B. Brambel<br>Logging Company</h1>
    </div>
  </section>

  <section class="card card-back" aria-label="Business card back">
    <div class="panel">
      <p class="owner-name">MARV BRAMBEL</p>
      <p class="owner-title">Owner</p>
      <p class="contact-line">936-402-5817</p>
      <p class="contact-line">www.mbrambellogging.example</p>
      <p class="contact-line">mbrambellogging@mailbox.example</p>
      <p class="contact-line">PO Box 8462 Cedar Hollow, Tx 75912</p>
    </div>
  </section>
</body>
</html>
```